quorVale - website to pay membership association fee

The main purpose of this site it to allow a pre-registered user to be able to view the membership fees for their membership association and pay the same in one of the ways offered by the portal.
You are required to create a graphical project only for the logon functions as a user, while omitting the back end/administration ones that will be decided later
The site, besides being responsive must be very intuitive in its function. The graphics must be bright.

Number of Pages Required

4 page

Requirements
Must have
• i need to see template for
• 1. Home page
• 2. Page after login. People can se one or more bill to Pay and decide to see more details or to pay.
• 3. Page to Pay. Choose the desired payment method five alternative

```html
<!DOCTYPE html>
<html lang="en">
<head>
<meta charset="utf-8">
<title>quorVale – Make a Payment</title>
<link rel="stylesheet" href="https://fonts.googleapis.com/css2?family=Fredoka:wght@400;500;600;700&family=Lato:wght@400;700&display=swap">
<style>
  :root {
    --blue: #1b9ad6;
    --green: #52ad47;
    --stone: #c9c4c3;
    --panel: #ececec;
    --white: #ffffff;
    --ink: #1a1a1a;
  }
  * { box-sizing: border-box; margin: 0; padding: 0; }
  html, body { width: 1007px; height: 1200px; overflow: hidden; background: var(--stone); }
  .page { position: relative; width: 1007px; height: 1200px; background: var(--stone); font-family: "Lato", Arial, sans-serif; }

  .topbar { position: absolute; left: 0; top: 0; width: 1007px; height: 68px; background: var(--blue); }
  .brand { position: absolute; left: 449px; top: -38px; width: 110px; height: 110px; border-radius: 50%; background: var(--white);
           display: flex; align-items: flex-end; justify-content: center; padding-bottom: 30px;
           font-family: "Fredoka", sans-serif; font-weight: 600; font-size: 22px; color: var(--blue); }

  .crumb { position: absolute; left: 102px; top: 68px; width: 803px; height: 40px; background: var(--panel);
           display: flex; align-items: center; padding-left: 22px;
           font-family: "Fredoka", sans-serif; font-weight: 500; font-size: 18px; color: var(--blue); letter-spacing: .5px; }
  .crumb::before { content: ""; width: 16px; height: 16px; border-radius: 50%; background: var(--green); margin-right: 26px; }

  .steps { position: absolute; left: 0; top: 0; width: 1007px; height: 290px; }
  .step { position: absolute; width: 104px; text-align: center; }
  .step svg { display: block; margin: 0 auto; }
  .step-label { display: block; margin-top: 4px; font-family: "Fredoka", sans-serif; font-weight: 500; font-size: 23px; letter-spacing: .5px; color: var(--blue); }
  .step.is-current .step-label { color: var(--green); }
  .step-arrow { position: absolute; }

  .section-title { position: absolute; left: 102px; top: 294px; width: 803px; height: 39px; background: var(--green);
                   color: var(--white); font-family: "Fredoka", sans-serif; font-weight: 600; font-size: 28px; letter-spacing: .5px;
                   text-align: center; line-height: 39px; }
  .bills-panel { position: absolute; left: 102px; top: 333px; width: 803px; height: 769px; background: var(--panel); }

  .bill { position: absolute; left: 64px; width: 676px; height: 314px; border: 2.5px dashed var(--blue); border-radius: 9px; }
  .bill-1 { top: 39px; }
  .bill-2 { top: 398px; }
  .bill-tag { position: absolute; left: 16px; top: 10px; width: 165px; height: 42px; background: var(--blue); color: var(--white);
              font-family: "Fredoka", sans-serif; font-weight: 600; font-size: 21px; line-height: 42px; padding-left: 13px; letter-spacing: .5px; }
  .bill-info { position: absolute; left: 15px; top: 74px; width: 362px; height: 166px; background: var(--white); }
  .bill-row { position: absolute; left: 17px; width: 330px; height: 34px; font-size: 16px; color: var(--ink); display: flex; align-items: center; }
  .bill-row .value { position: absolute; left: 150px; color: var(--green); font-size: 16px; }
  .bill-row svg { position: absolute; right: 4px; }
  .row-amount { top: 12px; }
  .row-due { top: 62px; }
  .row-paid { top: 113px; }
  .bill-institution { position: absolute; left: 408px; top: 74px; width: 247px; height: 166px; background: var(--white);
                      display: flex; align-items: center; justify-content: center; color: var(--green); font-size: 16px; }
  .bill-actions { position: absolute; left: 182px; top: 262px; display: flex; gap: 19px; }
  .btn { width: 144px; height: 37px; background: var(--blue); color: var(--white); font-family: "Fredoka", sans-serif; font-weight: 700;
         font-size: 30px; letter-spacing: 1.5px; line-height: 37px; text-align: center; }

  .footer { position: absolute; left: 2px; top: 1102px; width: 1005px; height: 98px; background: var(--blue); }
</style>
</head>
<body>
<div class="page">
  <header class="topbar">
    <div class="brand">quorVale</div>
  </header>

  <div class="crumb">Make a Payment</div>

  <nav class="steps" aria-label="Payment steps">
    <div class="step" style="left:163px; top:132px;">
      <svg width="110" height="110" viewBox="0 0 110 110" aria-hidden="true">
        <path d="M52 2a51 51 0 1 0 33 90l15 7-6-16A51 51 0 0 0 52 2z" fill="var(--blue)"/>
        <text x="52" y="54" text-anchor="middle" font-family="Fredoka, sans-serif" font-weight="700" font-size="33" fill="#fff">GET</text>
        <text x="52" y="76" text-anchor="middle" font-family="Fredoka, sans-serif" font-weight="600" font-size="14" fill="#fff">STRATED</text>
      </svg>
      <span class="step-label">Start</span>
    </div>
    <svg class="step-arrow" style="left:270px; top:170px;" width="56" height="26" viewBox="0 0 56 26" aria-hidden="true">
      <path d="M2 13h44M36 3l12 10-12 10" fill="none" stroke="#fff" stroke-width="6" stroke-linecap="round" stroke-linejoin="round"/>
    </svg>

    <div class="step is-current" style="left:327px; top:132px;">
      <svg width="110" height="110" viewBox="0 0 110 110" aria-hidden="true">
        <path d="M52 2a51 51 0 1 0 33 90l15 7-6-16A51 51 0 0 0 52 2z" fill="var(--green)"/>
        <path d="M36 45l16-13 10 11" fill="none" stroke="#fff" stroke-width="5" stroke-linejoin="round"/>
        <rect x="26" y="48" width="55" height="32" rx="3" fill="#fff"/>
        <rect x="32" y="54" width="8" height="4" fill="var(--green)"/>
        <circle cx="64" cy="72" r="3.5" fill="var(--green)"/><circle cx="70" cy="72" r="3.5" fill="var(--green)"/>
      </svg>
      <span class="step-label">Payment</span>
    </div>
    <svg class="step-arrow" style="left:461px; top:170px;" width="84" height="26" viewBox="0 0 84 26" aria-hidden="true">
      <path d="M8 13h68M18 3L6 13l12 10M66 3l12 10-12 10" fill="none" stroke="#fff" stroke-width="6" stroke-linecap="round" stroke-linejoin="round"/>
    </svg>

    <div class="step" style="left:574px; top:132px;">
      <svg width="110" height="110" viewBox="0 0 110 110" aria-hidden="true">
        <path d="M52 2a51 51 0 1 0 33 90l15 7-6-16A51 51 0 0 0 52 2z" fill="var(--blue)"/>
        <rect x="30" y="22" width="46" height="58" rx="6" fill="none" stroke="#fff" stroke-width="3.5"/>
        <g fill="none" stroke="#fff" stroke-width="3">
          <circle cx="40" cy="36" r="3"/><circle cx="40" cy="51" r="3"/><circle cx="40" cy="66" r="3"/>
          <path d="M48 36h20M48 51h14M48 66h8"/>
        </g>
        <path d="M62 72l18-18 6 6-18 18h-6z" fill="#fff"/>
      </svg>
      <span class="step-label">Review</span>
    </div>
    <svg class="step-arrow" style="left:682px; top:170px;" width="56" height="26" viewBox="0 0 56 26" aria-hidden="true">
      <path d="M2 13h44M36 3l12 10-12 10" fill="none" stroke="#fff" stroke-width="6" stroke-linecap="round" stroke-linejoin="round"/>
    </svg>

    <div class="step" style="left:740px; top:132px;">
      <svg width="110" height="110" viewBox="0 0 110 110" aria-hidden="true">
        <path d="M52 2a51 51 0 1 0 33 90l15 7-6-16A51 51 0 0 0 52 2z" fill="var(--blue)"/>
        <rect x="30" y="20" width="46" height="58" rx="6" fill="none" stroke="#fff" stroke-width="3.5"/>
        <g fill="none" stroke="#fff" stroke-width="3">
          <circle cx="40" cy="34" r="3"/><circle cx="40" cy="49" r="3"/><circle cx="40" cy="64" r="3"/>
          <path d="M48 34h20M48 49h20M48 64h8"/>
        </g>
        <circle cx="72" cy="73" r="12" fill="var(--blue)" stroke="#fff" stroke-width="3"/>
        <path d="M66 73l4 4 8-8" fill="none" stroke="#fff" stroke-width="3" stroke-linecap="round" stroke-linejoin="round"/>
      </svg>
      <span class="step-label">Confirm</span>
    </div>
  </nav>

  <h1 class="section-title">Bill To Pay</h1>

  <main class="bills-panel">
    <article class="bill bill-1">
      <div class="bill-tag">Bill 1:.....</div>
      <div class="bill-info">
        <div class="bill-row row-amount">Membership 2017<span class="value">$154.27</span>
          <svg width="34" height="34" viewBox="0 0 34 34" aria-hidden="true"><path d="M6 12l9-9 8 9" fill="none" stroke="#1a1a1a" stroke-width="3.5" stroke-linejoin="round"/><rect x="2" y="14" width="32" height="18" rx="1" fill="#1a1a1a"/><circle cx="24" cy="26" r="2" fill="#fff"/><circle cx="28" cy="26" r="2" fill="#fff"/></svg>
        </div>
        <div class="bill-row row-due">DUF-ON-31-December-2017
          <svg width="36" height="36" viewBox="0 0 36 36" aria-hidden="true"><circle cx="18" cy="18" r="17" fill="#1a1a1a"/><circle cx="18" cy="18" r="11" fill="none" stroke="#fff" stroke-width="2"/><path d="M18 11v8h6" fill="none" stroke="#fff" stroke-width="2"/></svg>
        </div>
        <div class="bill-row row-paid">PAIED:<span class="value">NO</span></div>
      </div>
      <div class="bill-institution">LOGO ISTITUTION</div>
      <div class="bill-actions"><div class="btn">DETAIL</div><div class="btn">PAY</div></div>
    </article>

    <article class="bill bill-2">
      <div class="bill-tag">Bill 2:.....</div>
      <div class="bill-info">
        <div class="bill-row row-amount">Membership 2017<span class="value">$154.27</span>
          <svg width="34" height="34" viewBox="0 0 34 34" aria-hidden="true"><path d="M6 12l9-9 8 9" fill="none" stroke="#1a1a1a" stroke-width="3.5" stroke-linejoin="round"/><rect x="2" y="14" width="32" height="18" rx="1" fill="#1a1a1a"/><circle cx="24" cy="26" r="2" fill="#fff"/><circle cx="28" cy="26" r="2" fill="#fff"/></svg>
        </div>
        <div class="bill-row row-due">DUF-ON-31-December-2017
          <svg width="36" height="36" viewBox="0 0 36 36" aria-hidden="true"><circle cx="18" cy="18" r="17" fill="#1a1a1a"/><circle cx="18" cy="18" r="11" fill="none" stroke="#fff" stroke-width="2"/><path d="M18 11v8h6" fill="none" stroke="#fff" stroke-width="2"/></svg>
        </div>
        <div class="bill-row row-paid">PAIED:<span class="value">NO</span></div>
      </div>
      <div class="bill-institution">LOGO ISTITUTION</div>
      <div class="bill-actions"><div class="btn">DETAIL</div><div class="btn">PAY</div></div>
    </article>
  </main>

  <footer class="footer"></footer>
</div>
</body>
</html>
```